Redesign two existing website pages and one new landing page for dental office

I need to redesign two webpages on my dental website, the Home page (http://brelvoortdental.com) and the Dental Implant Services page (http://www.brelvoortdental.com/dental-implant-services) and also create a landing page for the Dental Implant Services page.

Please use the same color scheme, slogans and subtitles for the redesign pages and create a reserved video spot on each page. The video spots should not be too big but not too small either and positioned in a central key location on each of the pages. The final redesigned pages should communicate leadership, confidence and trust.

The new landing page for the Dental implant Services page must not have any hyperlinks on the page and must entice the viewer to give name and email before downloading a "Free" eBook called "Is a Fresh Smile Worth Waiting For?" Any added photo images to this new page must be smiling.
Updates

Project Deadline Extended Reason: I got feedback that my project was not long enough so I'm extending it by 5 days. Added Thursday, April 16, 2015

Target Market(s)

People who are middle-age to seniors.

Industry/Entity Type

Dental

Coding

Coded - Design and coding required

Number of Pages Required

3 page

Requirements
Must have
• Compatible with existing website colors and theme.

```html
<!DOCTYPE html>
<html lang="en">
<head>
<meta charset="utf-8">
<title>Brelvoort Dental Care</title>
<link href="https://fonts.googleapis.com/css2?family=Merienda:wght@400;700&family=Lato:wght@400;700&display=swap" rel="stylesheet">
<style>
:root{
  --teal-dark:#2f5a4c;
  --teal-deep:#3c6a5c;
  --teal-mid:#7fa79c;
  --teal-soft:#8fb3aa;
  --teal-light:#a8c6bf;
  --ink:#222;
  --grey-text:#444;
  --line:#cfd8d5;
  --white:#fff;
}
*{margin:0;padding:0;box-sizing:border-box}
html,body{width:761px;height:1200px;overflow:hidden;background:var(--white)}
body{position:relative;font-family:"Lato",sans-serif;color:var(--ink)}
.abs{position:absolute}

/* header */
.site-header{left:0;top:0;width:761px;height:83px;background:linear-gradient(#fafbfb,#eef0f0);border-top:3px solid var(--teal-soft)}
.brand{left:71px;top:38px;font-family:"Merienda",cursive;font-size:18px;color:var(--teal-dark);white-space:nowrap}
.contact-item{top:16px;display:flex;align-items:center;gap:7px;font-size:9.5px;color:#333}
.contact-item .dot{width:20px;height:20px;border-radius:50%;background:var(--teal-deep);display:flex;align-items:center;justify-content:center}
.main-nav{right:72px;top:56px;display:flex;gap:12px;font-family:"Merienda",cursive;font-size:10.5px;color:var(--teal-dark)}
.main-nav .current{border-bottom:1px solid var(--teal-dark);padding-bottom:3px}

/* hero */
.hero{left:0;top:83px;width:761px;height:282px;background:linear-gradient(90deg,#d9e4ea 0%,#c4cfd4 35%,#b7bdbf 60%,#c4c8c9 100%)}
.hero-title{right:72px;top:112px;text-align:right;font-family:"Merienda",cursive;font-size:22px;line-height:39px;color:var(--teal-dark)}
.slider-arrows{display:flex;gap:4px}
.slider-arrows span{width:15px;height:15px;border:1.3px solid #666;border-radius:50%;display:flex;align-items:center;justify-content:center}

/* welcome */
.welcome{left:0;top:365px;width:761px;height:182px;text-align:center}
.section-title{font-family:"Merienda",cursive;font-size:19px;color:var(--teal-dark);display:flex;align-items:center;justify-content:center;gap:10px}
.section-title .rule{height:1px;width:105px;background:var(--line)}
.section-title em{font-style:normal;color:var(--teal-mid)}
.welcome .lead{font-size:14px;margin-top:10px;color:#222}
.welcome .body{font-size:8.7px;line-height:14.4px;color:var(--grey-text);width:620px;margin:6px auto 0}
.btn-learn{display:inline-block;margin-top:13px;background:var(--teal-deep);color:#fff;font-family:"Merienda",cursive;font-size:9px;padding:4px 9px;border-radius:2px}

/* services */
.services{left:0;top:547px;width:761px;height:240px;background:radial-gradient(ellipse at 75% 40%,#eef0f0 0%,#cfd3d2 40%,#b9a9a2 75%,#a99387 100%)}
.services .section-title{position:absolute;top:18px;left:0;width:761px;color:#fff}
.services .section-title .rule{background:#eee}
.card{top:87px;width:130px;height:126px;background:var(--teal-mid);border:1px solid #9bbcb3;text-align:center;color:#fff}
.card.active{background:linear-gradient(#7fa79c,#3f6b5e)}
.card h3{font-family:"Merienda",cursive;font-weight:400;font-size:16px;margin-top:38px}
.card p{font-size:8.3px;line-height:11.3px;margin:7px 10px 0}
.card .plus{position:absolute;left:53px;bottom:0;width:0;height:0;border-left:12px solid transparent;border-right:12px solid transparent;border-bottom:10px solid var(--teal-dark)}
.icon-ring{top:60px;width:54px;height:54px;border-radius:50%;background:#fff;border:2px solid var(--teal-dark);display:flex;align-items:center;justify-content:center}
.side-arrow{top:127px;width:26px;height:36px;background:#f4f4f4;display:flex;align-items:center;justify-content:center}

/* columns */
.col-title{top:814px;font-family:"Merienda",cursive;font-size:17px;color:var(--teal-dark)}
.col-title em{font-style:normal;color:#222}
.col-rule{top:846px;height:2px;background:#e3e8e6}
.photo{background:linear-gradient(135deg,#e9d8cf,#c9a79a 60%,#b8877c)}
.copy{font-size:8.8px;line-height:13.6px;color:var(--grey-text)}
.read{font-size:8px;color:#333}

/* cta */
.cta{left:0;top:984px;width:761px;height:62px;background:var(--teal-soft)}
.cta-text{left:82px;top:1012px;width:420px;font-family:"Merienda",cursive;font-size:11.3px;letter-spacing:-0.2px;color:#fff;white-space:nowrap}
.cta-btn{left:514px;top:1004px;width:175px;height:28px;background:#fff;font-family:"Merienda",cursive;font-size:12.5px;color:var(--teal-dark);display:flex;align-items:center;justify-content:center}

/* footer */
.footer{left:0;top:1046px;width:761px;height:124px;background:var(--teal-deep);color:#fff}
.foot-nav{left:71px;top:1065px;display:flex;gap:14px;font-size:8.5px}
.foot-rule{left:71px;top:1086px;width:455px;height:1px;background:#5f897c}
.foot-addr{left:71px;top:1096px;font-size:8.3px;line-height:13.6px}
.foot-contact{left:242px;top:1098px;font-size:8.3px;line-height:17.5px}
.foot-contact div{display:flex;align-items:center;gap:6px}
.email-field{left:377px;top:1099px;width:139px;height:19px;border:1px solid #cfdcd8;font-size:8px;color:#cfdcd8;padding:4px 8px}
.submit{left:377px;top:1126px;width:139px;height:19px;background:var(--teal-soft);border:1px solid #cfdcd8;font-size:8px;font-weight:700;display:flex;align-items:center;justify-content:center}
.foot-brand{left:577px;top:1096px;font-family:"Merienda",cursive;font-size:12px;color:#dfe9e6;white-space:nowrap}
.social{top:1130px;width:18px;height:18px;border-radius:50%;background:var(--teal-soft)}
.bottom-bar{left:0;top:1170px;width:761px;height:30px;background:var(--teal-soft);color:#fff}
</style>
</head>
<body>

<header class="site-header abs">
  <div class="brand abs">Brelvoort Dental Care</div>
  <div class="contact-item abs" style="left:453px">
    <span class="dot"><svg width="10" height="10" viewBox="0 0 10 10"><path d="M2 1l2 2-1 1.2c.6 1.3 1.5 2.2 2.8 2.8L7 6l2 2-1.3 1.3C4 9 1 6 .7 2.3z" fill="#fff"/></svg></span>(281) 555-0147
  </div>
  <div class="contact-item abs" style="left:560px">
    <span class="dot"><svg width="11" height="8" viewBox="0 0 11 8"><rect x=".5" y=".5" width="10" height="7" fill="none" stroke="#fff"/><path d="M.5 .5l5 4 5-4" fill="none" stroke="#fff"/></svg></span>info@brelvoortdental.com
  </div>
  <nav class="main-nav abs">
    <span class="current">Home</span><span>About Us</span><span>Dental Services</span><span>Blog</span><span>Contact Us</span><span>Testimonials</span>
  </nav>
</header>

<section class="hero abs" role="img" aria-label="Dentist in blue scrubs touching a glowing digital health interface">
  <div class="hero-title abs">Life-Changing Family<br>Dental Care In Sugar Land
    <div class="slider-arrows" style="justify-content:flex-end;margin-top:4px">
      <span><svg width="6" height="6"><path d="M4 0L1 3l3 3" fill="none" stroke="#555" stroke-width="1.3"/></svg></span>
      <span><svg width="6" height="6"><path d="M2 0l3 3-3 3" fill="none" stroke="#555" stroke-width="1.3"/></svg></span>
    </div>
  </div>
</section>

<section class="welcome abs">
  <h2 class="section-title" style="margin-top:25px;font-weight:400"><span class="rule"></span>Welcome To Brelvoort <em>Dental Care</em><span class="rule"></span></h2>
  <p class="lead">Duis autem vel eum iriure dolor in hendrerit in vulputate velit esse molestie consequat, velillum</p>
  <p class="body">Lorem ipsum dolor sit amet, consectetuer adipiscing elit, sed diam nonummy nibh euismod tincidunt ut laoreet dolore magna aliquam erat veolutpat. Ut wisi enim minim veniam, quis nostrud exerci tation ullamcorper suscipit lobortis nisl ut aliquip ex ea commodo consequat. Dolore eu feugiat nulla facilisis at vero eros et accumsan et iusto odio dignissim qui blandit praesent luptatum zzril delenit augue duis dolore te feugait nulla facilisi.</p>
  <span class="btn-learn">LEARN MORE</span>
</section>

<section class="services abs" role="img" aria-label="Soft-focus close-up of a large white tooth model">
  <h2 class="section-title" style="font-weight:400"><span class="rule"></span>Our Services<span class="rule"></span></h2>
  <div class="side-arrow abs" style="left:45px;border-radius:0 18px 18px 0"><svg width="8" height="12"><path d="M7 1L2 6l5 5" fill="none" stroke="#333" stroke-width="2.5"/></svg></div>
  <div class="side-arrow abs" style="left:692px;border-radius:18px 0 0 18px"><svg width="8" height="12"><path d="M1 1l5 5-5 5" fill="none" stroke="#333" stroke-width="2.5"/></svg></div>

  <div class="card active abs" style="left:93px"><h3>Hygiene</h3><p>Ut wisi enim ad mi erewnim veniam, quis nostrud exerc lobortis nislut commodo.</p><span class="plus"></span></div>
  <div class="card abs" style="left:241px"><h3>Emergencies</h3><p>Ut wisi enim ad mi erewnim veniam, quis nostrud exerc lobortis nislut commodo.</p><span class="plus"></span></div>
  <div class="card abs" style="left:389px"><h3>Implants</h3><p>Ut wisi enim ad mi erewnim veniam, quis nostrud exerc lobortis nislut commodo.</p><span class="plus"></span></div>
  <div class="card abs" style="left:537px"><h3>Cosmetic</h3><p>Ut wisi enim ad mi erewnim veniam, quis nostrud exerc lobortis nislut commodo.</p><span class="plus"></span></div>

  <div class="icon-ring abs" style="left:131px;top:60px"><svg width="30" height="30" viewBox="0 0 30 30"><circle cx="15" cy="15" r="13" fill="none" stroke="#2f5a4c" stroke-width="1.5"/><path d="M15 5c4 6 6 9 6 12a6 6 0 0 1-12 0c0-3 2-6 6-12z" fill="#2f5a4c"/></svg></div>
  <div class="icon-ring abs" style="left:279px;top:60px"><svg width="30" height="26" viewBox="0 0 30 26"><rect x="2" y="6" width="26" height="15" rx="2" fill="#2f5a4c"/><rect x="12" y="2" width="6" height="4" fill="#2f5a4c"/><path d="M15 9v9M10.5 13.5h9" stroke="#fff" stroke-width="3"/><circle cx="8" cy="22" r="3" fill="#2f5a4c" stroke="#fff"/><circle cx="22" cy="22" r="3" fill="#2f5a4c" stroke="#fff"/></svg></div>
  <div class="icon-ring abs" style="left:427px;top:60px"><svg width="24" height="30" viewBox="0 0 24 30"><path d="M4 2c4-1 6 1 8 1s4-2 8-1c3 1 3 7 0 9H4C1 9 1 3 4 2z" fill="none" stroke="#2f5a4c" stroke-width="2"/><path d="M6 14h12M7 18h10M8 22h8M10 26h4" stroke="#2f5a4c" stroke-width="2.5"/></svg></div>
  <div class="icon-ring abs" style="left:575px;top:60px"><svg width="26" height="30" viewBox="0 0 26 30"><path d="M5 3c4-2 6 1 8 1s4-3 8-1c4 2 3 9 1 13-1 3-1 11-4 11s-2-8-5-8-2 8-5 8-3-8-4-11C2 12 1 5 5 3z" fill="none" stroke="#2f5a4c" stroke-width="2.2"/></svg></div>
</section>

<h3 class="col-title abs" style="left:71px;font-weight:400">Don't Wait <em>'til It Hurts!</em></h3>
<div class="col-rule abs" style="left:71px;width:287px"></div>
<div class="photo abs" role="img" aria-label="Close-up of a smile during a dental mirror check" style="left:70px;top:861px;width:88px;height:106px"></div>
<p class="copy abs" style="left:171px;top:858px;width:195px">Lorem ipsum dolor sit amet, consectetuer erere adipiscing elit, sed diam nonummy nibh euismod tincidunt ut laoreet dolore magna aliquam erate volutpat. Ut wisi enim minim veniam, quis werwe nostrud exerci tation ullamcorper suscipit wrew volutpat. Ut wisi enim minim veniam, quis werwe nostrud exerci tation ullamcorper susci</p>
<span class="read abs" style="left:171px;top:960px">READ MORE+</span>

<div class="abs" style="left:379px;top:819px;width:1px;height:149px;background:#e3e8e6"></div>

<h3 class="col-title abs" style="left:407px;font-weight:400">Latest <em>Blog Posts</em></h3>
<div class="slider-arrows abs" style="left:663px;top:818px">
  <span style="width:12px;height:12px;border-color:#aaa"></span><span style="width:12px;height:12px;border-color:#666"><svg width="5" height="5"><path d="M1 0l3 2.5-3 2.5" fill="none" stroke="#555"/></svg></span>
</div>
<div class="col-rule abs" style="left:400px;width:289px;height:1px;background:#e6e9e8"></div>
<div class="col-rule abs" style="left:400px;width:174px;background:#cfd8d5"></div>

<div class="photo abs" role="img" aria-label="Patient in a dental chair during a check-up" style="left:401px;top:861px;width:69px;height:41px"></div>
<p class="copy abs" style="left:483px;top:859px;width:210px">Lorem ipsum dolor sit amet, consectetuer erere eri adipiscing elit, sed diam nonummy nibh eu...</p>
<span class="read abs" style="left:483px;top:894px">READ MORE+</span>
<div class="abs" style="left:400px;top:913px;width:289px;height:1px;border-top:1px dotted #ccc"></div>
<div class="photo abs" role="img" aria-label="Smiling patient in a dental chair" style="left:401px;top:926px;width:69px;height:41px"></div>
<p class="copy abs" style="left:483px;top:924px;width:210px">Lorem ipsum dolor sit amet, consectetuer erere eri adipiscing elit, sed diam nonummy nibh eu...</p>
<span class="read abs" style="left:483px;top:959px">READ MORE+</span>

<section class="cta abs"></section>
<div class="cta-text abs">Comprehensive Family Dentistry in One Sugar Land Dental Office!</div>
<div class="cta-btn abs">Schedule &amp; Appointment</div>

<footer class="footer abs"></footer>
<nav class="foot-nav abs" style="color:#fff">
  <span>Home</span><span>✕</span><span>About Us</span><span>✕</span><span>Dental Services</span><span>✕</span><span>Blog</span><span>✕</span><span>Contact Us</span><span>✕</span><span>Testimonials</span>
</nav>
<div class="foot-rule abs"></div>
<address class="foot-addr abs" style="font-style:normal;color:#fff"><b>Brelvoort Dental</b><br>Elmridge Street no 4180<br>Near wall street optisiho dollar Smt<br>nonumy - 334687</address>
<div class="foot-contact abs" style="color:#fff">
  <div><svg width="8" height="8" viewBox="0 0 10 10"><path d="M2 1l2 2-1 1.2c.6 1.3 1.5 2.2 2.8 2.8L7 6l2 2-1.3 1.3C4 9 1 6 .7 2.3z" fill="#fff"/></svg>+123 456 7890</div>
  <div><svg width="9" height="8" viewBox="0 0 9 8"><rect x="2" y="0" width="5" height="3" fill="#fff"/><rect x="0" y="3" width="9" height="3" fill="#fff"/><rect x="2" y="5" width="5" height="3" fill="none" stroke="#fff"/></svg>+123 456 7890</div>
  <div><svg width="9" height="7" viewBox="0 0 11 8"><rect x=".5" y=".5" width="10" height="7" fill="#fff"/><path d="M.5 .5l5 4 5-4" fill="none" stroke="#3c6a5c"/></svg>info@brelvoortdental.com</div>
</div>
<div class="email-field abs">Enter Your Email Here</div>
<div class="submit abs" style="color:#fff">SUBMIT</div>
<div class="foot-brand abs">Brelvoort Dental Care</div>
<span class="social abs" style="left:585px"></span>
<span class="social abs" style="left:608px"></span>
<span class="social abs" style="left:630px"></span>
<span class="social abs" style="left:653px"></span>

<div class="bottom-bar abs">
  <span class="abs" style="left:72px;top:10px;font-size:8.5px">© 2015 Brelvoort Dental, All Rights Reserved</span>
  <svg class="abs" style="left:528px;top:5px" width="13" height="21" viewBox="0 0 13 21"><rect x="1" y="1" width="11" height="19" rx="2" fill="none" stroke="#fff" stroke-width="1.5"/><circle cx="6.5" cy="16.5" r="1.2" fill="#fff"/></svg>
  <span class="abs" style="left:549px;top:8px;font-size:11px">Get Dr. Brelvoort's Mobile App</span>
</div>

</body>
</html>
```